Music teacher for flute, beinning piano and a Music and Movement class

I would like a QP page where folks could contact me for flute and beginning piano lessons OR for a Music and Movement class (low-impact exercises, singing, work with drumming/rhythms to alleviate the symptoms of Parkinson's disease.) I have a QP page for the Music and Movement but not for music lessons.
https://www.pagelinkr.example/ChimeandStrideOakvale
I would want a different url since I am no longer doing this in Roseville, CA but Sacramento, CA

Hello, forgive me for dropping out of contact. Can you tell me if there was a fake QP page created under the username Chime and Stride Birchford? It's surprisingly close to what I offer but it says "Painting class" and other misinformation. Any information would be helpful, thanks. I'd like to switch my username to Chime and Stride Birchford, if possible.

```html
<!DOCTYPE html>
<html lang="en">
<head>
<meta charset="utf-8">
<title>Chime and Stride Birchford – Music and Movement</title>
<link href="https://fonts.googleapis.com/css2?family=Quicksand:wght@400;500;600;700&display=swap" rel="stylesheet">
<style>
  :root {
    --page-bg: #e6fde0;
    --white: #ffffff;
    --banner-left: #29a6c0;
    --banner-right: #7ac561;
    --post-top: #0bb0e2;
    --post-bottom: #0a72bd;
    --post-blob: #1497c4;
    --post-teal: #18a3b8;
    --brand-teal: #2aa98f;
    --footer-text: #6f6f6f;
    --dot: #a8a8a8;
    --shadow: rgba(0, 0, 0, 0.18);
  }
  * { box-sizing: border-box; margin: 0; padding: 0; }
  html, body {
    width: 967px; height: 1200px; overflow: hidden;
    background: var(--page-bg);
    font-family: "Quicksand", sans-serif;
  }
  .canvas { position: relative; width: 967px; height: 1200px; }

  /* Cover banner */
  .cover {
    position: absolute; left: 42px; top: 53px; width: 659px; height: 254px;
    background: linear-gradient(100deg, var(--banner-left) 0%, #4bb6a2 45%, var(--banner-right) 100%);
    overflow: hidden; box-shadow: 0 2px 4px var(--shadow);
  }
  .cover-text { position: absolute; left: 0; top: 0; width: 350px; text-align: center; color: var(--white); }
  .cover-title {
    position: absolute; top: 86px; left: 0; width: 350px;
    font-size: 27px; font-weight: 700; letter-spacing: 0.3px;
  }
  .cover-subtitle {
    position: absolute; top: 123px; left: 0; width: 350px;
    font-size: 15.5px; font-weight: 700; letter-spacing: 0.4px;
  }
  .cover-line { position: absolute; left: 0; width: 350px; font-size: 14.3px; font-weight: 400; letter-spacing: 0.2px; }
  .cover-line.first { top: 155px; }
  .cover-line.second { top: 181px; }
  .cover-photo {
    position: absolute; border-radius: 50%;
    border: 7px solid var(--white);
    box-shadow: 0 2px 5px var(--shadow);
  }
  .cover-photo.drummer {
    left: 322px; top: -9px; width: 186px; height: 186px; z-index: 2;
    background:
      radial-gradient(circle at 20% 62%, rgba(240, 190, 120, 0.85) 0%, rgba(240, 190, 120, 0) 18%),
      radial-gradient(ellipse at 45% 78%, rgba(200, 60, 80, 0.55) 0%, rgba(200, 60, 80, 0) 35%),
      radial-gradient(circle at 75% 50%, rgba(150, 110, 90, 0.6) 0%, rgba(150, 110, 90, 0) 35%),
      linear-gradient(160deg, #10203a 0%, #1a1a2e 55%, #2a1420 100%);
  }
  .cover-photo.group {
    left: 443px; top: 50px; width: 206px; height: 206px; z-index: 1;
    background:
      radial-gradient(ellipse at 78% 38%, rgba(235, 205, 40, 0.8) 0%, rgba(235, 205, 40, 0) 28%),
      radial-gradient(ellipse at 40% 40%, rgba(40, 110, 170, 0.45) 0%, rgba(40, 110, 170, 0) 30%),
      linear-gradient(180deg, #ece9e3 0%, #d8d4cc 30%, #8c8f99 55%, #6a6c74 78%, #3e3f46 100%);
  }

  /* Brand tile */
  .brand-tile {
    position: absolute; left: 750px; top: 95px; width: 137px; height: 137px;
    background: var(--white); box-shadow: 0 1px 4px var(--shadow);
    display: flex; flex-direction: column; align-items: center; justify-content: center; gap: 8px;
  }
  .brand-dot { width: 16px; height: 16px; border-radius: 50%; background: var(--brand-teal); }
  .brand-name { color: var(--brand-teal); font-weight: 700; font-size: 17px; text-align: center; line-height: 1.15; }

  /* Post */
  .post {
    position: absolute; left: 42px; top: 352px; width: 776px; height: 776px;
    box-shadow: 0 2px 5px var(--shadow); background: var(--white);
  }
  .post-art {
    position: absolute; left: 0; top: 0; width: 776px; height: 705px; overflow: hidden;
    background: linear-gradient(180deg, var(--post-top) 0%, #0a8fd0 55%, var(--post-bottom) 100%);
  }
  .post-shapes { position: absolute; left: 0; top: 0; }
  .post-photo-frame {
    position: absolute; left: 23px; top: 36px; width: 731px; height: 511px;
    background: var(--white); padding: 10px;
  }
  .post-photo {
    width: 100%; height: 100%;
    background:
      radial-gradient(ellipse at 62% 60%, rgba(40, 100, 180, 0.85) 0%, rgba(40, 100, 180, 0) 20%),
      radial-gradient(ellipse at 50% 80%, rgba(70, 100, 150, 0.8) 0%, rgba(70, 100, 150, 0) 22%),
      radial-gradient(ellipse at 68% 105%, rgba(40, 180, 150, 0.9) 0%, rgba(40, 180, 150, 0) 22%),
      radial-gradient(ellipse at 85% 70%, rgba(170, 200, 225, 0.65) 0%, rgba(170, 200, 225, 0) 25%),
      radial-gradient(ellipse at 20% 85%, rgba(25, 25, 30, 0.85) 0%, rgba(25, 25, 30, 0) 35%),
      linear-gradient(180deg, #e4ddd1 0%, #cfc6b8 22%, #8f8a86 50%, #55545a 80%, #3a3a40 100%);
  }
  .post-title {
    position: absolute; left: 0; top: 577px; width: 776px; text-align: center;
    color: var(--white); font-weight: 700; font-size: 47px; letter-spacing: 1px;
  }
  .post-subtitle {
    position: absolute; left: 0; top: 638px; width: 776px; text-align: center;
    color: var(--white); font-weight: 500; font-size: 27px; letter-spacing: 0.8px;
  }
  .post-actions {
    position: absolute; left: 0; top: 705px; width: 776px; height: 71px;
    display: flex; align-items: center; padding: 0 24px;
    color: var(--footer-text); font-size: 14.5px; font-weight: 500;
  }
  .action-dot { width: 7px; height: 7px; border-radius: 50%; background: var(--dot); margin: 0 24px; }
  .comment-count { margin-left: auto; display: flex; align-items: center; gap: 6px; font-size: 16px; }
</style>
</head>
<body>
<main class="canvas">

  <section class="cover">
    <div class="cover-text">
      <h1 class="cover-title">MUSIC &amp; MOVEMENT</h1>
      <p class="cover-subtitle">FREEDOM OF EXPRESSION</p>
      <p class="cover-line first">USING MUSIC TO IMPROVE THE LIVES OF FOLKS</p>
      <p class="cover-line second">WITH PARKINSON'S DISEASE</p>
    </div>
    <div class="cover-photo group" role="img" aria-label="Class members standing together in a studio"></div>
    <div class="cover-photo drummer" role="img" aria-label="Drummer playing a drum kit on stage"></div>
  </section>

  <aside class="brand-tile">
    <span class="brand-dot"></span>
    <span class="brand-name">Chime and Stride<br>Birchford</span>
  </aside>

  <article class="post">
    <div class="post-art">
      <svg class="post-shapes" width="776" height="705" viewBox="0 0 776 705" aria-hidden="true">
        <path d="M0 0 H175 C195 40 210 90 210 140 L0 140 Z" fill="var(--post-blob)" opacity="0.6"/>
        <circle cx="880" cy="620" r="260" fill="var(--post-teal)" opacity="0.75"/>
      </svg>
      <div class="post-photo-frame">
        <div class="post-photo" role="img" aria-label="Seated group drumming with sticks on exercise balls"></div>
      </div>
      <h2 class="post-title">MUSIC AND MOVEMENT</h2>
      <p class="post-subtitle">FREEDOM OF EXPRESSION</p>
    </div>
    <footer class="post-actions">
      <span>Unlike</span><span class="action-dot"></span>
      <span>Comment</span><span class="action-dot"></span>
      <span>Share</span>
      <span class="comment-count">
        <svg width="20" height="18" viewBox="0 0 20 18" aria-hidden="true">
          <path d="M10 2 C15 2 18.5 4.8 18.5 8.2 C18.5 11.6 15 14.3 10 14.3 C8.8 14.3 7.7 14.2 6.7 13.9 L2.5 16 L3.6 12.4 C2.2 11.3 1.5 9.8 1.5 8.2 C1.5 4.8 5 2 10 2 Z" fill="none" stroke="var(--footer-text)" stroke-width="1.4"/>
        </svg>
        01
      </span>
    </footer>
  </article>

</main>
</body>
</html>
```